Business card design needed

We are 2 artists starting up a studio by the water in Sydney ...where we can work and display our art...would like the back ground to be Navy and white stripe...nautical...and the name The Clay Nook to be bold and the main wording...not nautical...if possible thought the A for art could be an easel ...ie the capital A using the cross bar as the platform that paint would be circles of colour....would like the main wording in Black but the easel A in colour
Hope u are able to help
thanku Lorna Vesk
as I will be away in a week for 4 weeks could u please send all info to Jodie Minchens email....she can contact me and we can go ahead asap....

Industry/Entity Type

Artists

Contact Information for Business Card

THE CLAY NOOK

Halloways Dock House
The Bend..41 Kelvane Rd..Mosman 2088 Sydney

Jodi Minchen..0417583091..jodiminchen@mailwave.example
Lorn Vesk...0413862714..lvesk@quillnet.example.au

```html
<!DOCTYPE html>
<html lang="en">
<head>
<meta charset="utf-8">
<title>The Clay Nook – Business Card</title>
<link rel="stylesheet" href="https://fonts.googleapis.com/css2?family=Fira+Sans:wght@400;700&display=swap">
<style>
  :root {
    --navy: #06304f;
    --white: #ffffff;
    --crimson: #c8103e;
    --ink: #111111;
    --card-text: #fbeef1;
  }
  * { margin: 0; padding: 0; box-sizing: border-box; }
  html, body {
    width: 1200px;
    height: 338px;
    overflow: hidden;
    background: var(--white);
  }
  .card {
    position: relative;
    width: 1200px;
    height: 338px;
    font-family: "Fira Sans", Arial, sans-serif;
  }
  .stripe-panel {
    position: absolute;
    left: 0;
    top: 0;
    width: 599px;
    height: 338px;
  }
  .brand-name {
    position: absolute;
    left: 167px;
    top: 126px;
    width: 268px;
    text-align: center;
    font-weight: 700;
    font-size: 36px;
    line-height: 44px;
    color: var(--ink);
  }
  .info-panel {
    position: absolute;
    left: 599px;
    top: 0;
    width: 601px;
    height: 338px;
    background: var(--crimson);
    color: var(--card-text);
    font-size: 15.5px;
    line-height: 23px;
  }
  .address {
    position: absolute;
    right: 285px;
    top: 147px;
    text-align: right;
    font-style: normal;
  }
  .divider {
    position: absolute;
    left: 330px;
    top: 65px;
    width: 2px;
    height: 207px;
    background: var(--card-text);
  }
  .contacts {
    position: absolute;
    left: 343px;
    top: 74px;
  }
  .contact + .contact { margin-top: 21px; }
  .contact-name { text-transform: uppercase; }
</style>
</head>
<body>
<div class="card">
  <svg class="stripe-panel" width="599" height="338" viewBox="0 0 599 338" aria-hidden="true">
    <rect width="599" height="338" fill="var(--white)"/>
    <g fill="var(--navy)">
      <rect x="0" y="14" width="599" height="34"/>
      <rect x="0" y="83" width="599" height="34"/>
      <rect x="0" y="152" width="599" height="34"/>
      <rect x="0" y="221" width="599" height="34"/>
      <rect x="0" y="290" width="599" height="34"/>
    </g>
    <circle cx="301" cy="170" r="134" fill="var(--ink)"/>
    <circle cx="301" cy="170" r="124" fill="var(--white)"/>
    <circle cx="301" cy="170" r="117" fill="none" stroke="var(--ink)" stroke-width="2"/>
  </svg>
  <div class="brand-name">The Clay<br>Nook</div>

  <section class="info-panel">
    <address class="address">
      Halloways Dock House, The Bend.<br>
      41 Kelvane Rd, Mosman 2088 Sydney
    </address>
    <div class="divider"></div>
    <div class="contacts">
      <div class="contact">
        <div class="contact-name">Jodi Minchen:</div>
        <div class="contact-phone">0417583091,</div>
        <div class="contact-email">jodiminchen@mailwave.example</div>
      </div>
      <div class="contact">
        <div class="contact-name">Lorn Vesk</div>
        <div class="contact-phone">0413862714,</div>
        <div class="contact-email">lvesk@quillnet.example.au</div>
      </div>
    </div>
  </section>
</div>
</body>
</html>
```